Horticulture Business Card Design Project

New garden service venture, I'd like design to reflect business name, Copper Lantern garden services. Needs to be professional non comical and include a pic. I'd like to see designs in browns and greens as it will be printed on recycled paper to promote sustainability. I'd prefer a modern professonal card that is simple and catchy.
Updates

Thank u to all that submitted design/s -I really appreciated all of them.

Target Market(s)

Professional people aged between 40-60, that own their own homes and enjoy their gardens. Wanting a premium service that can be recommended to others by handing out the card and conveying a professional card that is impressive to potential clients.

Industry/Entity Type

Business

Requirements
Must have
• Picture relating to horticulture. One sided and including business name- Copper Lantern Garden Services, Qualified Horticulturist, name, mobile number and email. Website is not needed. Id like a large green leaf pic such as monstera, ficus lyrata or rhaphis palms etc. Im open to ideas and welcome new suggestions. Simple fonts please
Nice to have
• Large green leaf as pic. Possibly like monstera or similar in size and impact. A modern touch
Should not have
• Comical pic

```html
<!DOCTYPE html>
<html lang="en">
<head>
<meta charset="utf-8">
<title>Copper Lantern Garden Services – Business Card</title>
<link rel="stylesheet" href="https://fonts.googleapis.com/css2?family=Crimson+Pro:wght@400;500;800&display=swap">
<style>
  :root {
    --page-bg: #ffffff;
    --leaf-light: #e4f0a8;
    --leaf-mid: #c8e280;
    --leaf-deep: #a9d456;
    --brand-brown: #3a2414;
    --rule-brown: #8a5a2b;
    --detail-rust: #7a2e12;
  }
  html, body {
    margin: 0;
    padding: 0;
    width: 911px;
    height: 1200px;
    overflow: hidden;
    background: var(--page-bg);
  }
  .canvas {
    position: relative;
    width: 911px;
    height: 1200px;
    font-family: "Crimson Pro", Georgia, serif;
  }
  .leaf-photo {
    position: absolute;
    left: 115px;
    top: 70px;
    width: 680px;
    height: 1060px;
    border-radius: 48% 48% 46% 46% / 38% 38% 40% 40%;
    background: radial-gradient(ellipse at 50% 50%, var(--leaf-light) 0%, var(--leaf-mid) 70%, var(--leaf-deep) 100%);
  }
  .brand {
    position: absolute;
    left: 163px;
    top: 340px;
    width: 583px;
    text-align: right;
    color: var(--brand-brown);
  }
  .brand__name {
    margin: 0;
    font-weight: 800;
    font-size: 116px;
    line-height: 0.84;
    letter-spacing: -1px;
    text-align: center;
    padding-left: 40px;
  }
  .brand__tagline {
    margin: 14px 0 0;
    font-weight: 500;
    font-size: 64px;
    line-height: 1;
    text-align: center;
  }
  .brand-rule {
    position: absolute;
    left: 163px;
    top: 628px;
    width: 583px;
    height: 10px;
    background: var(--rule-brown);
  }
  .contact {
    position: absolute;
    right: 230px;
    top: 676px;
    margin: 0;
    text-align: right;
    font-style: normal;
  }
  .contact__name {
    margin: 0 0 16px;
    font-weight: 500;
    font-size: 52px;
    line-height: 1;
    color: var(--brand-brown);
  }
  .contact__line {
    margin: 0;
    font-weight: 500;
    font-size: 40px;
    line-height: 54px;
    color: var(--detail-rust);
  }
</style>
</head>
<body>
<main class="canvas">
  <div class="leaf-photo" role="img" aria-label="Photograph of a large green fig leaf forming the card background"></div>
  <header class="brand">
    <h1 class="brand__name">Copper<br>Lantern</h1>
    <p class="brand__tagline">Garden Services</p>
  </header>
  <div class="brand-rule"></div>
  <address class="contact">
    <p class="contact__name">NAME</p>
    <p class="contact__line">Qualified Horticulturist</p>
    <p class="contact__line">Mobile</p>
    <p class="contact__line">Email</p>
  </address>
</main>
</body>
</html>
```